Design a product reviews website

We need a website design and simple logo for the brand Quelvio.com. The website will provide reviews of technology products and services. The brand and website should be approachable but should also be trustworthy and high quality. The deliverable should be designs, specs and assets that I can provide to a development team to build the website.

Target Market(s)

People researching products to buy.

Industry/Entity Type

Product

Logo Text

Quelvio.com

Number of Pages Required

5+ page

Font styles to use
Sans Serif

Colors
0492cd
0355a3
3176b5
33a6d7
85cae6
85abd2
cedeed
cee9f5

Requirements
Must have
• - Designs for the Homepage, Category and Article pages.
• - Designs for web and mobile.
• - Designs details for the engineering team to use for development.
• - I'm open to other colors than the preferences I chose but I'm more likely to like blues, greys and blacks.

```html
<!DOCTYPE html>
<html lang="en">
<head>
<meta charset="utf-8">
<title>Quelvio.com – Product Reviews</title>
<link rel="stylesheet" href="https://fonts.googleapis.com/css2?family=Lato:ital,wght@0,300;0,400;0,700;1,400&display=swap">
<style>
:root{
  --blue:#3a87d9;
  --blue-deep:#0492cd;
  --ink:#222;
  --text:#555;
  --muted:#777;
  --line:#d8d8d8;
  --panel:#f3f3f3;
  --white:#fff;
  --footer:#2b2b2b;
  --load:#8c8c8c;
}
*{box-sizing:border-box;margin:0;padding:0}
html,body{width:786px;height:1200px;overflow:hidden;background:var(--white);font-family:"Lato",sans-serif;color:var(--ink)}
.page{position:relative;width:786px;height:1200px}
.abs{position:absolute}

.site-header{left:0;top:0;width:786px;height:55px;border-bottom:2px solid var(--blue-deep);background:var(--white)}
.brand{left:68px;top:16px;display:flex;align-items:center;gap:6px;font-size:19px;font-weight:700;color:#1b2a3a;letter-spacing:.2px}
.brand-mark{width:14px;height:14px;border-radius:50%;background:var(--blue-deep)}
.menu-toggle{left:720px;top:20px}

.hero{left:0;top:55px;width:786px;height:296px;background:radial-gradient(ellipse at 55% 50%,#5d5a55 0%,#3a3430 45%,#1f1a17 100%)}
.hero-title{left:0;top:78px;width:786px;text-align:center;color:var(--white);font-weight:300;font-size:24px;line-height:27px;padding-left:30px}
.search{left:243px;width:254px;height:26px;background:var(--white);font:400 9px "Lato",sans-serif;color:#999;padding-left:10px;display:flex;align-items:center}
.search-btn{left:501px;width:37px;height:26px;background:var(--blue-deep);display:flex;align-items:center;justify-content:center}

.cat-nav{left:45px;top:386px;width:131px;border:1px solid var(--line);list-style:none}
.cat-nav li{height:31.6px;border-top:1px solid var(--line);display:flex;align-items:center;font-size:9px;color:#333;padding-left:8px;gap:10px}
.cat-nav li:first-child{border-top:none;background:var(--blue);color:var(--white)}
.cat-nav svg{width:22px;height:18px;flex:none}

.panel{border:1px solid var(--line);background:var(--panel)}
.panel-title{height:29px;border-bottom:1px solid var(--line);background:var(--white);font-size:11.5px;font-weight:700;padding-left:15px;line-height:29px;letter-spacing:.2px}
.new-products{left:198px;top:386px;width:355px;height:722px}
.popular{left:574px;top:386px;width:170px;height:722px}
.popular .panel-title{padding-left:11px}

.card{background:var(--white)}
.photo{position:absolute;left:0;top:0;width:100%}
.tags{position:absolute;right:10px;display:flex;gap:4px}
.tag{background:var(--blue);color:var(--white);font-size:9.5px;font-weight:700;padding:0 9px;height:21px;line-height:21px}
.card-title{position:absolute;left:8px;font-size:9.5px;color:var(--text)}
.byline{position:absolute;left:8px;right:10px;border-top:1px solid #e5e5e5;display:flex;align-items:center;padding-top:6px}
.avatar{width:27px;height:29px;background:linear-gradient(#cfcfcf,#9a9a9a)}
.author{color:var(--blue);font-size:11px;margin-left:5px}
.posted{margin-left:auto;font-style:italic;font-size:8px;color:var(--muted)}
.excerpt{position:absolute;left:7px;font-size:9.5px;line-height:14px;color:var(--text)}

.load-more{left:198px;top:1120px;width:546px;height:31px;background:var(--load);color:var(--white);display:flex;align-items:center;justify-content:center;gap:8px;font-size:10px;font-weight:700}
.site-footer{left:0;top:1168px;width:786px;height:32px;background:var(--footer);color:#ddd;font-size:8.5px;text-align:center;line-height:32px}
</style>
</head>
<body>
<div class="page">

<header class="site-header abs">
  <div class="brand abs"><span class="brand-mark"></span>Quelvio.com</div>
  <svg class="menu-toggle abs" width="15" height="12" viewBox="0 0 15 12" fill="#1b2a3a">
    <rect x="0" y="0" width="3" height="3"/><rect x="4" y="0" width="11" height="3"/>
    <rect x="0" y="4.5" width="3" height="3"/><rect x="4" y="4.5" width="11" height="3"/>
    <rect x="0" y="9" width="3" height="3"/><rect x="4" y="9" width="11" height="3"/>
  </svg>
</header>

<section class="hero abs" role="img" aria-label="Photo of a grey wireless speaker on a dark table">
  <h1 class="hero-title abs">The Best Product And Services Reviews<br>And Rankings</h1>
  <div class="search abs" style="top:166px">Search</div>
  <div class="search-btn abs" style="top:166px">
    <svg width="12" height="12" viewBox="0 0 12 12" fill="none" stroke="#fff" stroke-width="2"><circle cx="5" cy="5" r="3.6"/><path d="M7.7 7.7L11 11"/></svg>
  </div>
</section>

<ul class="cat-nav abs">
  <li><svg viewBox="0 0 22 18" fill="#fff"><path d="M11 2L2 10h3v6h4v-4h4v4h4v-6h3z"/></svg>HOME</li>
  <li><svg viewBox="0 0 22 18" fill="#555"><rect x="6" y="1" width="11" height="16" rx="2"/><rect x="9" y="6" width="5" height="4" fill="#fff"/></svg>APPLIANCES</li>
  <li><svg viewBox="0 0 22 18" fill="none" stroke="#555" stroke-width="1.3"><rect x="3" y="2" width="16" height="10"/><path d="M8 16h6M11 12v4"/></svg>COMPUTERS</li>
  <li><svg viewBox="0 0 22 18" fill="#555"><rect x="1" y="4" width="20" height="10" rx="2"/><circle cx="14" cy="9" r="3" fill="#fff"/><rect x="4" y="7" width="5" height="1.3" fill="#fff"/><rect x="4" y="10" width="5" height="1.3" fill="#fff"/></svg>ELECTRONICS</li>
  <li><svg viewBox="0 0 22 18" fill="none" stroke="#555" stroke-width="1.2"><path d="M2 9l7-7 7 7M4 8v8h8"/><path d="M14 9l4-1 3 1v4c0 2-3 4-3 4s-4-2-4-4z"/></svg>HOME SECURITY</li>
  <li><svg viewBox="0 0 22 18" fill="none" stroke="#555" stroke-width="1.3"><rect x="7" y="1" width="8" height="16" rx="1.5"/><path d="M10 14h2"/></svg>MOBILES</li>
  <li><svg viewBox="0 0 22 18" fill="none" stroke="#555" stroke-width="1.2"><path d="M3 9l8-7 8 7M5 8v9h12V8"/><rect x="9" y="10" width="4" height="4"/></svg>SMART HOME</li>
  <li><svg viewBox="0 0 22 18" fill="none" stroke="#555" stroke-width="1.2"><rect x="7" y="5" width="8" height="8"/><path d="M4 7h3M4 9h3M4 11h3M15 7h3M15 9h3M15 11h3M9 2v3M11 2v3M13 2v3M9 13v3M11 13v3M13 13v3"/></svg>SOFTWARE</li>
</ul>

<section class="new-products panel abs">
  <h2 class="panel-title">NEW PRODUCTS</h2>

  <article class="card abs" style="left:11px;top:42px;width:331px;height:236px">
    <div class="photo" style="height:159px;background:linear-gradient(#a0522d,#7a4a2e 60%,#9a7650)" role="img" aria-label="Living room with a wall-mounted TV and tower speakers"></div>
    <div class="tags" style="top:127px"><span class="tag">HOME</span><span class="tag">SPEAKERS</span></div>
    <p class="card-title" style="top:171px">Lorem Ipsum Dolor Sit Amet</p>
    <div class="byline" style="top:189px"><span class="avatar" role="img" aria-label="Author portrait"></span><span class="author">Mark Ellison</span><span class="posted">Posted On 11 Aug, 2016</span></div>
  </article>

  <article class="card abs" style="left:11px;top:294px;width:154px;height:164px">
    <div class="photo" style="height:120px;background:linear-gradient(90deg,#8a8478,#dcdcd8 60%,#eeeeec)" role="img" aria-label="Hand pressing a wall-mounted smart home touch panel"></div>
    <div class="tags" style="top:92px"><span class="tag">HOME</span></div>
    <p class="excerpt" style="top:127px">Lorem ipsum dolor sit amet,<br>consectetuer elit</p>
  </article>

  <article class="card abs" style="left:188px;top:294px;width:154px;height:164px">
    <div class="photo" style="height:120px;background:linear-gradient(135deg,#f4f4f4,#e2e2e2 50%,#f7f7f7)" role="img" aria-label="Smartphone and smartwatch on a white background"></div>
    <div class="tags" style="top:92px"><span class="tag">HOME</span></div>
    <p class="excerpt" style="top:127px">Lorem ipsum dolor sit amet,<br>consectetuer elit</p>
  </article>

  <article class="card abs" style="left:11px;top:479px;width:331px;height:235px">
    <div class="photo" style="height:159px;background:linear-gradient(90deg,#6b3a2a,#1c1c1c 20%,#111 70%,#5a4030)" role="img" aria-label="Black wireless music system on a wooden table"></div>
    <div class="tags" style="top:127px"><span class="tag">AUDIO</span></div>
    <p class="card-title" style="top:171px">Lorem Ipsum Dolor Sit Amet</p>
    <div class="byline" style="top:189px"><span class="avatar" role="img" aria-label="Author portrait"></span><span class="author">Mark Ellison</span><span class="posted">Posted On 11 Aug, 2016</span></div>
  </article>
</section>

<aside class="popular panel abs">
  <h2 class="panel-title">POPULAR PRODUCTS</h2>
  <article class="card abs" style="left:11px;top:42px;width:147px;height:156px">
    <div class="photo" style="height:111px;background:linear-gradient(#2a2a2a,#a0683c 60%,#3a3a3a)" role="img" aria-label="Copper cookware set"></div>
    <div class="tags" style="top:80px"><span class="tag">HOME</span></div>
    <p class="excerpt" style="top:119px">Lorem ipsum dolor sit<br>amet, consectetuer</p>
  </article>
  <article class="card abs" style="left:11px;top:214px;width:147px;height:156px">
    <div class="photo" style="height:111px;background:linear-gradient(#cfcfcf,#7c7870 50%,#8a5a30)" role="img" aria-label="Kitchen sink with a steel faucet"></div>
    <div class="tags" style="top:80px"><span class="tag">HOME</span></div>
    <p class="excerpt" style="top:119px">Lorem ipsum dolor sit<br>amet, consectetuer</p>
  </article>
  <article class="card abs" style="left:11px;top:386px;width:147px;height:156px">
    <div class="photo" style="height:111px;background:linear-gradient(135deg,#d9a02a,#3b6a8a 50%,#1d4fa0)" role="img" aria-label="Tablet with a blue keyboard cover"></div>
    <div class="tags" style="top:80px"><span class="tag">HOME</span></div>
    <p class="excerpt" style="top:119px">Lorem ipsum dolor sit<br>amet, consectetuer</p>
  </article>
  <article class="card abs" style="left:11px;top:558px;width:147px;height:156px">
    <div class="photo" style="height:111px;background:linear-gradient(90deg,#6a7e92,#c8ced4 40%,#2a2a2a 70%,#8896a4)" role="img" aria-label="Keypad door lock"></div>
    <div class="tags" style="top:80px"><span class="tag">HOME</span></div>
    <p class="excerpt" style="top:119px">Lorem ipsum dolor sit<br>amet, consectetuer</p>
  </article>
</aside>

<div class="load-more abs">
  <svg width="16" height="16" viewBox="0 0 16 16" fill="none" stroke="#fff" stroke-width="1.6"><path d="M13.5 6A6 6 0 0 0 2.5 5M2.5 10a6 6 0 0 0 11 1"/><path d="M2 2v3.5h3.5M14 14v-3.5h-3.5"/></svg>
  Load More
</div>

<footer class="site-footer abs">Copyright © 2016 &nbsp;Quelvio.com. All Rights Reserved.</footer>
</div>
</body>
</html>
```